Vantrel Telecom Corporate Website & Social Branding

We are looking for a new website for our startup telecom which provides UCaaS, SD-WAN, Business SMS/MMS, Video Conferencing, Managed Network Service & more.

Target Market(s)

Small offices from 1-250 users

Industry/Entity Type

Telecomunications

Coding

Coded - Design and coding required

Colors
0054AA
0677BA
7BADD7
CADEEF
E8F1F8

```html
<!DOCTYPE html>
<html lang="en">
<head>
<meta charset="utf-8">
<title>Vantrel Telecom</title>
<link href="https://fonts.googleapis.com/css2?family=Poppins:wght@400;500;600;700&display=swap" rel="stylesheet">
<style>
:root{
  --navy:#0054AA;
  --blue:#0677BA;
  --sky:#7BADD7;
  --pale:#CADEEF;
  --mist:#E8F1F8;
  --ink:#111111;
  --text:#333333;
  --white:#ffffff;
}
*{box-sizing:border-box;margin:0;padding:0}
html,body{width:1200px;height:3507px;overflow:hidden}
body{font-family:'Poppins',sans-serif;color:var(--ink);background:var(--white);position:relative}
.abs{position:absolute}
a{color:inherit;text-decoration:none}
.btn{display:inline-flex;align-items:center;justify-content:center;background:var(--navy);color:var(--white);font-weight:500;border-radius:2px;box-shadow:0 4px 8px rgba(0,40,90,.3)}
.accent{color:var(--blue)}

/* top bar */
.topbar{left:0;top:0;width:1200px;height:52px;background:var(--blue);color:var(--white);font-size:16px}
.topbar .item{position:absolute;top:0;height:52px;display:flex;align-items:center;gap:9px}
.topbar svg{width:18px;height:18px;fill:var(--white)}

/* nav */
.nav{left:0;top:52px;width:1200px;height:68px}
.logo{display:flex;align-items:center;gap:8px;font-weight:700;color:var(--navy);font-size:25px}
.logo .dot{width:26px;height:26px;border-radius:50%;background:var(--blue)}
.nav .logo{position:absolute;left:110px;top:14px}
.menu{position:absolute;left:337px;top:0;height:68px;display:flex;align-items:center;gap:40px;font-size:18px;font-weight:500}
.menu .active{color:var(--navy);font-weight:600}
.menu .caret::after{content:"";display:inline-block;width:5px;height:5px;border-right:1.5px solid #333;border-bottom:1.5px solid #333;transform:rotate(45deg);margin-left:7px;vertical-align:4px}
.nav .demo{position:absolute;left:928px;top:12px;width:161px;height:42px;font-size:18px;gap:10px;box-shadow:none}

/* hero */
.hero{left:0;top:120px;width:1200px;height:598px;overflow:hidden}
.hero svg.bg{position:absolute;left:0;top:0}
.hero h1{position:absolute;left:62px;top:128px;font-size:48px;font-weight:600;line-height:52px}
.hero p{position:absolute;left:62px;top:240px;width:400px;font-size:18px;line-height:26px;color:var(--text)}
.hero .btn{position:absolute;left:64px;top:336px;width:171px;height:61px;font-size:21px}
.dots{position:absolute;left:62px;top:452px;display:flex;gap:20px;align-items:center}
.dots span{width:10px;height:10px;border-radius:50%;background:var(--blue)}
.dots .on{width:14px;height:14px;background:var(--white);border:3px solid var(--blue)}

/* services */
.services-title{left:0;top:800px;width:1200px;text-align:center;font-size:33px;font-weight:600}
.card{width:314px;height:179px;background:var(--white);border:1px solid #dcdcdc;box-shadow:0 2px 8px rgba(0,0,0,.12)}
.card.featured{border-color:var(--navy)}
.card .icon{position:absolute;left:12px;top:22px;width:68px;height:68px;border-radius:50%;background:var(--white);box-shadow:0 2px 8px rgba(0,0,0,.14);display:flex;align-items:center;justify-content:center}
.card .icon svg{width:40px;height:40px;stroke:var(--navy);fill:none;stroke-width:1.8}
.card h3{position:absolute;left:106px;top:22px;font-size:19px;font-weight:600}
.card.featured h3{color:var(--navy)}
.card p{position:absolute;left:106px;top:52px;width:195px;font-size:12px;line-height:20px;color:var(--text)}
.card .btn{position:absolute;left:106px;top:126px;width:117px;height:40px;font-size:15px;font-weight:400;box-shadow:none}

/* mission */
.mission{left:0;top:1362px;width:1200px;height:672px;overflow:hidden;background:var(--mist)}
.mission svg{position:absolute;left:0;top:0}
.panel{position:absolute;top:134px;width:328px;height:393px;background:var(--white);box-shadow:0 6px 20px rgba(0,0,0,.12);padding:44px 32px 0}
.panel .ring{width:60px;height:60px;border-radius:50%;background:var(--pale);display:flex;align-items:center;justify-content:center}
.panel .ring svg{position:static;width:34px;height:34px;stroke:var(--navy);fill:none;stroke-width:1.8}
.panel h2{font-size:28px;font-weight:600;margin-top:18px}
.panel p{font-size:14.5px;line-height:26px;color:var(--text);margin-top:10px}
.panel .btn{width:137px;height:44px;font-size:17px;margin-top:14px}
.panel.right{text-align:right}
.panel.right .ring{margin-left:auto}

/* why */
.why-photo{left:110px;top:2133px;width:419px;height:393px;background:linear-gradient(135deg,#8a6f5c,#c9a98c 45%,#e7d9c6 75%,#9db3c6)}
.why{left:609px;top:2128px;width:478px}
.why h2{font-size:32px;font-weight:600}
.why h4{font-size:21px;font-weight:600;line-height:29px;margin-top:22px;text-align:justify;text-align-last:left}
.why p{font-size:17.5px;line-height:29px;margin-top:10px;text-align:justify;color:var(--text)}
.why .btn{width:172px;height:64px;font-size:21px;margin-top:34px}

/* touch */
.touch{left:0;top:2619px;width:1200px;height:422px;background:linear-gradient(180deg,#0a74bb 0%,#0a6db3 60%,#075ea6 100%);color:var(--white);text-align:center}
.touch h2{margin-top:80px;font-size:31px;font-weight:500}
.touch p{width:740px;margin:26px auto 0;font-size:21px;line-height:28px}
.touch p b{font-weight:600}
.touch p u{text-underline-offset:4px}
.subscribe{position:absolute;left:302px;top:263px;display:flex;gap:16px}
.subscribe .field{width:386px;height:67px;background:var(--white);display:flex;align-items:center;gap:12px;padding-left:26px;color:#555;font-size:15px}
.subscribe .field svg{width:20px;height:16px;stroke:#555;fill:none;stroke-width:1.4}
.subscribe .btn{width:194px;height:67px;font-size:20px;font-weight:600;box-shadow:none}

/* footer */
.footer-brand{left:110px;top:3140px;width:210px}
.footer-brand .logo{font-size:30px}
.footer-brand .logo .dot{width:32px;height:32px}
.footer-brand p{margin-top:22px;font-size:15.5px;line-height:26px;color:var(--text);font-weight:500}
.social{display:flex;gap:20px;margin-top:16px;padding-left:6px}
.social span{width:29px;height:29px;border-radius:50%;background:var(--navy)}
.fcol h5{font-size:21px;font-weight:600}
.fcol ul{list-style:none;margin-top:16px}
.fcol li{font-size:15.5px;line-height:34.5px;color:var(--text);font-weight:500;display:flex;align-items:center;gap:10px}
.fcol li::before{content:"";width:5px;height:5px;border-right:1.8px solid #222;border-bottom:1.8px solid #222;transform:rotate(-45deg)}
.fcol .bar{width:32px;height:2px;background:var(--ink);margin-top:14px}
.contact li::before{display:none}
.contact li{align-items:flex-start;line-height:24px;margin-bottom:12px}
.contact svg{width:14px;height:14px;margin-top:5px;stroke:#333;fill:none;stroke-width:1.6;flex:none}
.rule{left:110px;top:3411px;width:978px;height:1px;background:#888}
.copy{left:110px;top:3443px;font-size:15.5px;font-weight:500}
.bottom-links{left:686px;top:3443px;display:flex;gap:52px;font-size:15.5px;font-weight:500}
</style>
</head>
<body>

<div class="abs topbar">
  <div class="item" style="left:110px"><svg viewBox="0 0 24 24"><path d="M6.6 10.8a15 15 0 0 0 6.6 6.6l2.2-2.2a1 1 0 0 1 1-.25 11.4 11.4 0 0 0 3.6.57 1 1 0 0 1 1 1V20a1 1 0 0 1-1 1A17 17 0 0 1 3 4a1 1 0 0 1 1-1h3.5a1 1 0 0 1 1 1c0 1.25.2 2.45.57 3.57a1 1 0 0 1-.25 1z"/></svg>(555) 240-7310</div>
  <div class="item" style="left:358px;font-size:15px"><svg viewBox="0 0 24 24"><path d="M12 3a8 8 0 0 0-8 8v6a2 2 0 0 0 2 2h2v-7H6v-1a6 6 0 0 1 12 0v1h-2v7h2v1h-5v2h5a2 2 0 0 0 2-2v-9a8 8 0 0 0-8-8z"/></svg>Support</div>
  <div class="item" style="left:547px;font-size:15px"><svg viewBox="0 0 24 24"><path d="M3 7h12a1 1 0 0 1 1 1v8a1 1 0 0 1-1 1H3a1 1 0 0 1-1-1V8a1 1 0 0 1 1-1zm14 3 5-3v10l-5-3z"/></svg>Join a Meeting</div>
  <div class="item" style="left:772px;font-size:15px"><span style="font-size:18px">$</span>Billing Center</div>
  <div class="item" style="left:1020px;font-size:15px"><svg viewBox="0 0 24 24"><circle cx="12" cy="7" r="4.5"/><path d="M3 21a9 7 0 0 1 18 0z"/></svg>Login</div>
</div>

<header class="abs nav">
  <div class="logo"><span class="dot"></span>Vantrel</div>
  <nav class="menu">
    <a class="active">Home</a>
    <a class="caret">About</a>
    <a class="caret" style="margin-left:-12px">Services</a>
    <a style="margin-left:-6px">Testimonials</a>
    <a>Contact us</a>
  </nav>
  <a class="btn demo">View Demo <svg width="18" height="12" viewBox="0 0 18 12"><path d="M0 6h16M11 1l5 5-5 5" stroke="#fff" stroke-width="1.8" fill="none"/></svg></a>
</header>

<section class="abs hero">
  <svg class="bg" width="1200" height="598" viewBox="0 0 1200 598">
    <defs>
      <linearGradient id="heroPhoto" x1="0" y1="0" x2="1" y2="1">
        <stop offset="0" stop-color="#d9e3ec"/>
        <stop offset=".45" stop-color="#9aa8b6"/>
        <stop offset=".75" stop-color="#5b5f66"/>
        <stop offset="1" stop-color="#2f3338"/>
      </linearGradient>
    </defs>
    <polygon points="422,0 500,0 640,295 415,598 335,598 562,295" fill="var(--pale)"/>
    <polygon points="500,0 1200,0 1200,598 415,598 640,295" fill="url(#heroPhoto)" role="img" aria-label="Photo of two colleagues in an office shaking hands"/>
  </svg>
  <h1>Welcome To<br><span class="accent">Vantrel</span> Telecom</h1>
  <p>Duis aute irure dolor in rhenderit in voluptae velit cillum dolore nulla pariatur. Excepteur sint occaecat cupidatat .</p>
  <a class="btn">Get Started</a>
  <div class="dots"><span></span><span></span><span class="on"></span><span></span><span></span></div>
</section>

<h2 class="abs services-title">Services <span class="accent">We Provide</span></h2>

<div class="abs card" style="left:110px;top:882px">
  <div class="icon"><svg viewBox="0 0 40 40"><circle cx="20" cy="20" r="7"/><circle cx="20" cy="20" r="13" stroke-dasharray="5 3"/><circle cx="20" cy="20" r="17"/></svg></div>
  <h3>UCaaS</h3><p>Excepteur sint occaecat cupidatat non proident, sunt deserunt mollit anim.</p><a class="btn">Learn More</a>
</div>
<div class="abs card" style="left:442px;top:882px">
  <div class="icon"><svg viewBox="0 0 40 40"><path d="M6 11h28M6 20h28M6 29h28"/><circle cx="14" cy="11" r="3" fill="#fff"/><circle cx="26" cy="20" r="3" fill="#fff"/><circle cx="16" cy="29" r="3" fill="#fff"/></svg></div>
  <h3>SD-WAN</h3><p>Duis aute irure dolor in reperit in voluptate velit esse cillum dolore eu fugiat nulla.</p><a class="btn">Learn More</a>
</div>
<div class="abs card" style="left:773px;top:882px">
  <div class="icon"><svg viewBox="0 0 40 40"><circle cx="20" cy="20" r="11"/><path d="M20 3v5M20 32v5M3 20h5M32 20h5M8 8l3.5 3.5M28.5 28.5 32 32M8 32l3.5-3.5M28.5 11.5 32 8M14 24l4-4 3 3 5-6"/></svg></div>
  <h3>Business SMS</h3><p>Nemo enim ipsam voluatem quia voluptas sit aspernatur aut odit aut fugit, sed quia</p><a class="btn">Learn More</a>
</div>
<div class="abs card" style="left:110px;top:1086px">
  <div class="icon"><svg viewBox="0 0 40 40"><path d="M5 35h30M8 35v-8h4v8M15 35v-12h4v12M22 35v-15h4v15M29 35v-20h4v20M8 20 18 12l5 4 10-10M28 6h5v5"/></svg></div>
  <h3>Business MMS</h3><p>Neque porro quisquam est, qui dolorem ipsum quia dolor sit amet, consectetur.</p><a class="btn">Learn More</a>
</div>
<div class="abs card featured" style="left:442px;top:1086px">
  <div class="icon"><svg viewBox="0 0 40 40"><circle cx="20" cy="20" r="17" fill="var(--navy)" stroke="none"/><rect x="11" y="15" width="13" height="10" rx="2" fill="#fff" stroke="none"/><path d="M25 18l5-3v10l-5-3z" fill="#fff" stroke="none"/></svg></div>
  <h3>Video Conferencing</h3><p>Quis autm vel eum iure reprit qui in ea voluate velit esse quam nihil molestiae.</p><a class="btn">Learn More</a>
</div>
<div class="abs card" style="left:773px;top:1086px">
  <div class="icon"><svg viewBox="0 0 40 40"><circle cx="20" cy="20" r="16"/><ellipse cx="20" cy="20" rx="7" ry="16"/><path d="M4 20h32M7 12h26M7 28h26"/></svg></div>
  <h3>Network Service</h3><p>Nemo enim ipsam voluatem quia voluptas sit aspernatur aut odit aut fugit, sed quia</p><a class="btn">Learn More</a>
</div>

<section class="abs mission">
  <svg width="1200" height="672" viewBox="0 0 1200 672">
    <defs>
      <linearGradient id="leftPhoto" x1="0" y1="0" x2="1" y2="1">
        <stop offset="0" stop-color="#3e4a3c"/><stop offset=".5" stop-color="#8a7a6c"/><stop offset="1" stop-color="#c9ccd0"/>
      </linearGradient>
      <linearGradient id="rightPhoto" x1="1" y1="0" x2="0" y2="1">
        <stop offset="0" stop-color="#3a3835"/><stop offset=".5" stop-color="#9c8a78"/><stop offset="1" stop-color="#c7b9a8"/>
      </linearGradient>
    </defs>
    <polygon points="0,0 380,0 565,336 463,672 0,672" fill="url(#leftPhoto)" role="img" aria-label="Photo of a smiling man on a phone call at a laptop"/>
    <polygon points="820,0 1200,0 1200,672 760,672 635,336" fill="url(#rightPhoto)" role="img" aria-label="Photo of two colleagues reviewing a tablet together"/>
  </svg>
  <div class="panel" style="left:219px">
    <div class="ring"><svg viewBox="0 0 34 34"><circle cx="17" cy="17" r="13"/><circle cx="17" cy="17" r="8"/><circle cx="17" cy="17" r="3"/><path d="M17 17 29 5"/></svg></div>
    <h2>Our <span class="accent">Mission</span></h2>
    <p>Neque porro quisquam est, qui dolorem ipsum quia dolor sit amet, consectetur, adipisci velit, et dolore magnam aliquam quaerat voluptatem.</p>
    <a class="btn">Learn More</a>
  </div>
  <div class="panel right" style="left:652px">
    <div class="ring"><svg viewBox="0 0 34 34"><path d="M6 10h22M6 17h22M6 24h22"/><circle cx="13" cy="10" r="2.5" fill="#CADEEF"/><circle cx="22" cy="17" r="2.5" fill="#CADEEF"/><circle cx="14" cy="24" r="2.5" fill="#CADEEF"/></svg></div>
    <h2>Our <span class="accent">Vission</span></h2>
    <p>Nemo enim ipsam voluptatem quia voluptas sit aspernatur aut odit aut fugit, sed quia consetur magni dolores eos qui ratione voluptatem sequi nesciunt..</p>
    <a class="btn">Learn More</a>
  </div>
</section>

<div class="abs why-photo" role="img" aria-label="Photo of a smiling team gathered around a desk"></div>
<section class="abs why">
  <h2>Why <span class="accent">Choose Us</span></h2>
  <h4>Excepteur sint occaecat cupidatat non proident,deserunt mollit laborum.</h4>
  <p>Temporibus autem quibusdam et aut officiis debitis aut rerum necessitatibus saepe eveniet ut et voluptates repudiandae sint et molestiae non recusandae. Itaque earum rerum hic tenetur a sapiente delectus, ut aut reiciendis voluptatibus maiores alias consequatur aut perferendis.</p>
  <a class="btn">Read More</a>
</section>

<section class="abs touch">
  <h2>Get In Touch</h2>
  <p>Our Vantrel Telecom services is available monday to saturday. If you need urgent assistance use this service, <b>Call (555) 240-7310</b> or emergeny call <u>(555) 240-7311</u></p>
  <form class="subscribe">
    <div class="field"><svg viewBox="0 0 20 16"><rect x="1" y="1" width="18" height="14"/><path d="M1 1l9 8 9-8"/></svg>Enter Email Address</div>
    <a class="btn">SUBSCRIBE</a>
  </form>
</section>

<div class="abs footer-brand">
  <div class="logo"><span class="dot"></span>Vantrel</div>
  <p>Excepteur sint occaecat cup idatat non proident, sut deserunt mollit anim id est laborum.</p>
  <div class="social"><span></span><span></span><span></span><span></span></div>
</div>
<div class="abs fcol" style="left:374px;top:3142px">
  <h5>Quick Links</h5>
  <ul><li>Home</li><li>About</li><li>Services</li><li>Testimonials</li><li>Contact us</li></ul>
</div>
<div class="abs fcol" style="left:579px;top:3140px">
  <h5>Services</h5>
  <ul><li>UCaaS</li><li>SD-WAN</li><li>Business SMS/MMS</li><li>Video Conferencing</li><li>Managed Network Service</li></ul>
</div>
<div class="abs fcol contact" style="left:854px;top:3142px">
  <h5>Contact us</h5>
  <div class="bar"></div>
  <ul style="margin-top:20px">
    <li><svg viewBox="0 0 14 14"><path d="M3.5 1.5 5.5 4 4.3 5.5a8 8 0 0 0 4.2 4.2L10 8.5l2.5 2-1 2A10.5 10.5 0 0 1 1.5 2.5z"/></svg>(555) 240-7311</li>
    <li><svg viewBox="0 0 14 14"><circle cx="7" cy="5" r="3"/><path d="M2 13c1-3 9-3 10 0"/></svg>Suite 14 Harbor Lane,<br>Brookvale, NY 10482</li>
    <li><svg viewBox="0 0 14 14"><rect x="1" y="3" width="12" height="9"/><path d="M1 3l6 5 6-5"/></svg>hello@vantreltelecom.com</li>
  </ul>
</div>
<div class="abs rule"></div>
<div class="abs copy">Copyrights@2022.All Rights Reserved</div>
<nav class="abs bottom-links"><a>Home</a><a>Services</a><a>About</a><a>Contact us</a></nav>

</body>
</html>
```